どの案も素敵でしたが、こちらの作品が最もイメージにあっていました。
皆様ご提案ありがとうございました。どれも個性的で良い提案ばかりでした。また機会があれば依頼させていただきますのでよろしくお願いいたします。
書籍の表紙デザイン案のお願い そよ風の“こもれび”手帖 バナー作成・バナーデザインの仕事の依頼

```html
<!DOCTYPE html>
<html lang="ja">
<head>
<meta charset="UTF-8">
<title>そよ風の“こもれび”手帖</title>
<link href="https://fonts.googleapis.com/css2?family=M+PLUS+Rounded+1c:wght@500;700;800&family=Zen+Maru+Gothic:wght@700;900&display=swap" rel="stylesheet">
<style>
  :root {
    --teal: #4dbdc0;
    --teal-deep: #2fa6ab;
    --ink: #262626;
    --orange: #ec8a2c;
    --orange-soft: #f2b27a;
    --white: #ffffff;
    --band: #e2e46a;
    --marker: #f4f2a4;
  }
  * { margin: 0; padding: 0; box-sizing: border-box; }
  html, body { width: 749px; height: 1200px; overflow: hidden; background: var(--teal); }
  .cover {
    position: relative; width: 749px; height: 1200px; overflow: hidden;
    background: var(--teal);
    font-family: "Zen Maru Gothic", "M PLUS Rounded 1c", sans-serif;
    color: var(--ink);
  }
  .backdrop-art {
    position: absolute; inset: 0 0 294px 0;
    background: linear-gradient(160deg, #56c3c5, #45b7ba);
  }
  .cloud-art {
    position: absolute; left: 80px; top: 40px; width: 533px; height: 235px;
    background: var(--white); border-radius: 118px;
  }
  .house-art {
    position: absolute; left: 107px; top: 300px; width: 533px; height: 606px;
    background: var(--white);
  }
  .tagline {
    position: absolute; left: 80px; width: 533px; top: 88px;
    text-align: center; color: var(--orange);
    font-weight: 900; font-size: 52px; line-height: 66px; letter-spacing: 2px;
    transform: rotate(-4deg);
  }
  .title { position: absolute; left: 107px; width: 533px; text-align: center; font-weight: 900; }
  .title-lead { top: 395px; font-size: 68px; letter-spacing: 4px; }
  .title-main { top: 480px; font-size: 92px; letter-spacing: 4px; }
  .title-main .accent {
    color: var(--orange);
    background: linear-gradient(transparent 80%, var(--marker) 80%);
  }
  .title-boxes {
    position: absolute; top: 640px; left: 107px; width: 533px;
    display: flex; justify-content: center; gap: 16px;
  }
  .title-boxes span {
    width: 130px; height: 124px; border: 6px solid var(--teal-deep);
    background: #eef9f9; color: var(--teal-deep);
    font-size: 90px; font-weight: 900; line-height: 110px; text-align: center;
  }
  .figure { position: absolute; background: var(--orange-soft); border-radius: 40px 40px 12px 12px; }
  .figure-left { left: 8px; top: 660px; width: 92px; height: 300px; }
  .figure-right { left: 649px; top: 660px; width: 92px; height: 300px; }
  .band { position: absolute; left: 0; top: 906px; width: 749px; height: 294px; background: var(--band); }
  .points { position: absolute; left: 38px; top: 990px; list-style: none; }
  .points li {
    display: flex; align-items: center; gap: 14px; height: 92px;
    font-family: "M PLUS Rounded 1c", sans-serif; font-weight: 800; font-size: 46px;
  }
  .points .label { background: linear-gradient(transparent 62%, var(--marker) 62%); padding: 0 4px; }
  .points svg { width: 52px; height: 52px; flex: none; }
</style>
</head>
<body>
<div class="cover">
  <div class="backdrop-art" role="img" aria-label="淡い線画の洗濯物と時計のイラスト"></div>
  <div class="house-art" role="img" aria-label="煙突のある白い家のイラスト"></div>
  <div class="cloud-art" role="img" aria-label="白い雲と煙のイラスト"></div>

  <p class="tagline">共働きでも<br>家が回る！</p>

  <div class="title title-lead">そよ風の</div>
  <div class="title title-main"><span class="accent">こもれび</span></div>
  <div class="title-boxes"><span>手</span><span>帖</span></div>

  <div class="band"></div>
  <div class="figure figure-left" role="img" aria-label="モップを持つエプロン姿の人物のイラスト"></div>
  <div class="figure figure-right" role="img" aria-label="掃除機をかけるエプロン姿の人物のイラスト"></div>

  <ul class="points">
    <li>
      <svg viewBox="0 0 52 52"><circle cx="26" cy="26" r="24" fill="var(--orange)"/><path d="M15 27 L23 35 L38 18" fill="none" stroke="var(--white)" stroke-width="6" stroke-linecap="round" stroke-linejoin="round"/></svg>
      <span class="label">家族みんなが動ける仕組み</span>
    </li>
    <li>
      <svg viewBox="0 0 52 52"><circle cx="26" cy="26" r="24" fill="var(--orange)"/><path d="M15 27 L23 35 L38 18" fill="none" stroke="var(--white)" stroke-width="6" stroke-linecap="round" stroke-linejoin="round"/></svg>
      <span class="label">無理なく続く暮らしのコツ</span>
    </li>
  </ul>
</div>
</body>
</html>
```